Business Card Design

I would like a logo created for the top left corner of the card please. I would like a checkerboard in a dark navy with the edges fading out and one random bright orange square.
Updates

I have attached some further notes and a really rough sketch of what I am after.  Thank you. :)

Target Market(s)

Construction, mining, mechanical

Industry/Entity Type

Business

Contact Information for Business Card

Korvane Works Pty Ltd, Glen Hadwick, P. 0418365072, F. 0736209158, E.glen@korvaneworks.com.au, PO Box 87 YARRAWONGA Q 4581, ABN 53209874611

Font styles to use
Sans Serif

Requirements
Must have
• Really Dark Navy
Really bright Orange

```html
<!DOCTYPE html>
<html lang="en">
<head>
<meta charset="utf-8">
<title>Korvane Works Pty Ltd – Business Cards</title>
<link rel="stylesheet" href="https://fonts.googleapis.com/css2?family=Arimo:wght@700&family=Poiret+One&display=swap">
<style>
  :root {
    --navy: #0b1a3a;
    --ink: #0d0f14;
    --orange: #e8761a;
    --paper: #ffffff;
    --backdrop: #e4e4e2;
    --text-dark: #111111;
    --text-light: #f4f4f4;
  }
  html, body {
    margin: 0;
    width: 1200px;
    height: 900px;
    overflow: hidden;
    background: var(--backdrop);
  }
  .stage {
    position: relative;
    width: 1200px;
    height: 900px;
  }
  .card {
    position: absolute;
    left: 340px;
    width: 520px;
    height: 318px;
    border-radius: 14px;
    overflow: hidden;
    box-shadow: 0 2px 6px rgba(0,0,0,0.15);
  }
  .card--dark { top: 100px; background: var(--ink); color: var(--text-light); }
  .card--light { top: 482px; background: var(--paper); color: var(--text-dark); }

  .brand {
    position: absolute;
    left: 30px;
    top: 34px;
    display: flex;
    align-items: center;
    gap: 14px;
  }
  .brand__mark {
    width: 34px;
    height: 34px;
    background: var(--orange);
  }
  .brand__name {
    font-family: "Arimo", sans-serif;
    font-weight: 700;
    font-size: 30px;
    color: var(--orange);
    letter-spacing: -0.3px;
  }

  .person {
    position: absolute;
    left: 250px;
    top: 128px;
  }
  .person__name {
    font-family: "Poiret One", sans-serif;
    font-size: 40px;
    line-height: 1;
    margin: 0;
    letter-spacing: 1px;
  }
  .person__phone {
    font-family: "Poiret One", sans-serif;
    font-size: 20px;
    margin: 10px 0 0 50px;
    letter-spacing: 1.5px;
  }

  .contact {
    position: absolute;
    left: 30px;
    bottom: 42px;
    margin: 0;
    font-family: "Arimo", sans-serif;
    font-weight: 700;
    font-size: 14px;
    line-height: 1.2;
    letter-spacing: 1px;
  }
  .contact__line { display: block; }

  .card__band {
    position: absolute;
    left: 0;
    right: 0;
    bottom: 0;
    height: 18px;
    background: var(--orange);
  }
</style>
</head>
<body>
<main class="stage">

  <section class="card card--dark" aria-label="Business card, dark side">
    <div class="brand">
      <span class="brand__mark"></span>
      <span class="brand__name">Korvane Works Pty Ltd</span>
    </div>
    <div class="person">
      <h1 class="person__name">Glen Hadwick</h1>
      <p class="person__phone">0418 365 072</p>
    </div>
    <address class="contact">
      <span class="contact__line">PO Box 87 YARRAWONGA Q 4581</span>
      <span class="contact__line">P. 0418 365 072</span>
      <span class="contact__line">F. 07 3620 9158</span>
      <span class="contact__line">E. glen@korvaneworks.com.au</span>
      <span class="contact__line">ABN 53 209 874 611</span>
    </address>
    <div class="card__band"></div>
  </section>

  <section class="card card--light" aria-label="Business card, light side">
    <div class="brand">
      <span class="brand__mark"></span>
      <span class="brand__name">Korvane Works Pty Ltd</span>
    </div>
    <div class="person">
      <h2 class="person__name">Glen Hadwick</h2>
      <p class="person__phone">0418 365 072</p>
    </div>
    <address class="contact">
      <span class="contact__line">PO Box 87 YARRAWONGA Q 4581</span>
      <span class="contact__line">P. 0418 365 072</span>
      <span class="contact__line">F. 07 3620 9158</span>
      <span class="contact__line">E. glen@korvaneworks.com.au</span>
      <span class="contact__line">ABN 53 209 874 611</span>
    </address>
    <div class="card__band"></div>
  </section>

</main>
</body>
</html>
```